Redesign of Business Card to look more professional and stand out

Business card design. You can lean more about our company by going to dlmfabworks.example. Raised letters would be nice. Company name & Address
DL&M
418 Wrenfield Crest Drive, Suite 140
Birmingham, AL 35999

You can use my name and title: Glenn Marlowe
Business Development Manager

Target Market(s)

Heavy Industrial market, i.e. utilities, chemical plants, paper mills, construction companies

Industry/Entity Type

Construction

Contact Information for Business Card

We provide Project Management & Project Support Services

Font styles to use
Serif

Requirements
Must have
• Company name & Address
• DL&M
• 418 Wrenfield Crest Drive, Suite 140
• Birmingham, AL 35999
Nice to have
• ideas for the back of the card
Should not have
• no crazy colors. needs to look professional and standout.

```html
<!DOCTYPE html>
<html lang="en">
<head>
<meta charset="utf-8">
<title>DL&amp;M Business Card</title>
<link href="https://fonts.googleapis.com/css2?family=Montserrat:wght@700&family=Questrial&display=swap" rel="stylesheet">
<style>
  :root {
    --navy: #1c3a6c;
    --cream: #eeece1;
    --cream-text: #efeee2;
    --ink: #2d2d2d;
    --backdrop: #d9dadc;
  }
  * { margin: 0; padding: 0; box-sizing: border-box; }
  html, body { width: 1200px; height: 786px; overflow: hidden; }
  body {
    background: var(--backdrop);
    font-family: "Questrial", "Century Gothic", sans-serif;
    position: relative;
  }
  .card {
    position: absolute;
    top: 244px;
    width: 520px;
    height: 297px;
    border-radius: 16px;
    overflow: hidden;
    box-shadow: 0 6px 18px rgba(0,0,0,0.18);
  }
  /* Front */
  .card--front { left: 50px; background: var(--cream); color: var(--ink); }
  .front__swoosh { position: absolute; left: 0; bottom: 0; width: 260px; height: 200px; }
  .front__company {
    position: absolute; left: 38px; top: 60px;
    font-family: "Questrial", sans-serif;
    font-weight: 400;
    font-size: 52px;
    line-height: 1;
    color: var(--navy);
    letter-spacing: 2px;
  }
  .front__details { position: absolute; left: 262px; top: 96px; width: 240px; }
  .person__name {
    font-family: "Montserrat", sans-serif;
    font-weight: 700;
    font-size: 15px;
    color: var(--navy);
    text-transform: uppercase;
    letter-spacing: 0.5px;
  }
  .person__title { font-size: 13px; margin-top: 3px; }
  .contact-list { list-style: none; margin-top: 14px; font-size: 12.5px; line-height: 18px; }
  .contact-list li { display: flex; align-items: center; gap: 7px; }
  .contact-list svg { width: 13px; height: 13px; flex: none; }
  .address { font-size: 12.5px; line-height: 17px; margin-top: 12px; }
  /* Back */
  .card--back { left: 630px; background: var(--navy); color: var(--cream-text); text-align: center; }
  .back__company {
    margin-top: 82px;
    font-family: "Questrial", sans-serif;
    font-weight: 400;
    font-size: 60px;
    line-height: 1;
    letter-spacing: 3px;
  }
  .back__web { font-size: 15px; margin-top: 8px; letter-spacing: 0.5px; }
  .back__services { font-size: 12.5px; line-height: 18px; margin-top: 34px; letter-spacing: 0.6px; }
</style>
</head>
<body>
  <section class="card card--front">
    <svg class="front__swoosh" viewBox="0 0 260 200" aria-hidden="true">
      <path d="M0 60 C60 120 150 170 260 200 L0 200 Z" fill="var(--navy)"/>
      <path d="M0 80 C70 140 150 180 230 200 L215 200 C140 182 60 148 0 100 Z" fill="#ffffff" opacity="0.85"/>
    </svg>
    <div class="front__company">DL&amp;M</div>
    <div class="front__details">
      <div class="person__name">Glenn Marlowe</div>
      <div class="person__title">Business Development Manager</div>
      <ul class="contact-list">
        <li>
          <svg viewBox="0 0 13 13"><rect width="13" height="13" rx="2" fill="var(--navy)"/><path d="M4 3 L5.5 3 L6 5 L5 5.8 C5.5 7 6.2 7.7 7.2 8 L8 7 L10 7.5 L10 9 C6.5 9.5 3.5 6.5 4 3 Z" fill="var(--cream)"/></svg>
          05-555-0148
        </li>
        <li>
          <svg viewBox="0 0 13 13"><rect width="13" height="13" rx="2" fill="var(--navy)"/><rect x="3" y="4" width="7" height="5" fill="none" stroke="var(--cream)" stroke-width="1"/><path d="M3 4 L6.5 7 L10 4" fill="none" stroke="var(--cream)" stroke-width="1"/></svg>
          info@dlmfabworks.example
        </li>
        <li>
          <svg viewBox="0 0 13 13"><rect width="13" height="13" rx="2" fill="var(--navy)"/><circle cx="6.5" cy="6.5" r="3.5" fill="none" stroke="var(--cream)" stroke-width="1"/><path d="M3 6.5 H10 M6.5 3 V10" stroke="var(--cream)" stroke-width="0.8"/></svg>
          www.dlmfabworks.example
        </li>
      </ul>
      <p class="address">418 Wrenfield Crest Drive, Suite 140<br>Birmingham, AL 35999</p>
    </div>
  </section>

  <section class="card card--back">
    <div class="back__company">DL&amp;M</div>
    <div class="back__web">www.dlmfabworks.example</div>
    <p class="back__services">Project Management · Constructability · Planning &amp; Scheduling<br>Consulting · Estimating · Cost Control · Training · Project Planning</p>
  </section>
</body>
</html>
```